DLM Homepage Banner

I would like a banner that uses/interprets the existing graphic on the www.janetholmcounsel.example homepage.

Target Market(s)

Business professionals across a variety of industries and sectors.

Requirements
Must have
• Must incorporate all the words and relationships of the existing image (file attached). I am seeking a professional and clean interpretation of the image.
• Must consider the look and feel of the banner on the following page: http://www.janetholmcounsel.example/pathways-in-nordic-crm/ (file attached)
• Must include the DLM logo in a similar style to the banner on the Pathways in Nordic CRM page (file attached).
Nice to have
• Feel free to add background/foreground graphics.
• I like the design idea of "bio-mechanical" applied to a professional services/business industry.
• The overall image must display a "business-technology-people-change" balance.
Should not have
• Should not be a direct replication of the existing graphic but must contain all the words and relationships.

```html
<!DOCTYPE html>
<html lang="en">
<head>
<meta charset="utf-8">
<title>DLM Homepage Banner</title>
<link rel="stylesheet" href="https://fonts.googleapis.com/css2?family=Montserrat:wght@500;600&family=Open+Sans:wght@400;600;700&display=swap">
<style>
  :root {
    --bg-light: #eef1f4;
    --bg-mid: #dde2e8;
    --navy: #1f3a6e;
    --orange: #f0820f;
    --link-blue: #2a6fd0;
    --arrow-grey: #d6d2cf;
    --arrow-edge: #c4bfbb;
    --ring-dark: #17509c;
    --ring-mid: #1c5fb6;
    --ring-light: #2d82e2;
    --cog: #143f80;
    --hub: #dfe5ec;
    --hub-line: #a9bcd6;
    --vein: #5d8fd0;
    --white: #ffffff;
  }
  * { margin: 0; padding: 0; box-sizing: border-box; }
  html, body { width: 1200px; height: 672px; overflow: hidden; }
  body { background: var(--bg-light); }
  .banner {
    position: relative;
    width: 1200px;
    height: 672px;
    overflow: hidden;
    background: radial-gradient(ellipse at 50% 45%, var(--bg-light) 0%, var(--bg-mid) 100%);
    font-family: "Open Sans", Arial, sans-serif;
  }
  .artwork { position: absolute; inset: 0; }

  /* bio-mechanical layer */
  .vein { fill: none; stroke: var(--vein); stroke-width: 1.4; opacity: 0.28; }
  .vein-node { fill: var(--bg-light); stroke: var(--vein); stroke-width: 1.4; opacity: 0.5; }
  .drive-chain { fill: none; stroke: var(--navy); stroke-width: 5; stroke-dasharray: 9 5; opacity: 0.18; }
  .cog-teeth { fill: none; stroke: var(--cog); stroke-width: 13; stroke-dasharray: 18 22.2; }
  .segment { fill: url(#ringFill); stroke: var(--white); stroke-width: 2; stroke-linejoin: round; }
  .hub { fill: var(--hub); }
  .hub-iris { fill: none; stroke: var(--hub-line); stroke-width: 6; stroke-dasharray: 3 7; }
  .hub-orbit { fill: none; stroke: var(--hub-line); stroke-width: 1.2; }
  .hub-core { fill: var(--hub-line); }
  .connector { stroke: var(--navy); stroke-width: 1.4; fill: none; opacity: 0.8; }
  .flow-arrow { fill: var(--arrow-grey); }
  .flow-seam { stroke: var(--arrow-edge); stroke-width: 1.5; fill: none; }
  .flow-rivet { fill: var(--arrow-edge); }

  .ring-label {
    font-family: "Montserrat", Arial, sans-serif;
    font-weight: 500;
    font-size: 20px;
    letter-spacing: 1px;
    fill: var(--white);
  }

  .heading {
    position: absolute;
    transform: translateX(-50%);
    text-align: center;
    color: var(--navy);
    white-space: nowrap;
  }
  .heading-title { font-size: 22px; font-weight: 700; line-height: 26px; }
  .heading-sub { font-size: 15px; font-weight: 600; line-height: 19px; margin-top: 2px; }
  .heading--procurement { left: 244px; top: 60px; }
  .heading--independence { left: 578px; top: 30px; }
  .heading--business { left: 911px; top: 60px; }

  .domain-list {
    position: absolute;
    left: 460px;
    top: 177px;
    width: 237px;
    list-style: none;
    border-top: 1.5px solid var(--orange);
  }
  .domain-list li {
    height: 48.5px;
    line-height: 48px;
    padding-left: 8px;
    border-bottom: 1.5px solid var(--orange);
    color: var(--orange);
    font-size: 19.5px;
    font-weight: 600;
    letter-spacing: 0.2px;
    white-space: nowrap;
    background: var(--bg-light);
  }
  .roles {
    position: absolute;
    left: 502px;
    top: 460px;
    list-style: none;
    color: var(--link-blue);
    font-size: 16px;
    line-height: 23px;
  }
  .brand {
    position: absolute;
    left: 866px;
    top: 598px;
    display: flex;
    align-items: center;
    gap: 12px;
    color: var(--navy);
    font-size: 27px;
    font-weight: 600;
    white-space: nowrap;
  }
  .brand-square { width: 26px; height: 26px; background: var(--navy); }
</style>
</head>
<body>
<main class="banner">
  <svg class="artwork" width="1200" height="672" viewBox="0 0 1200 672" aria-hidden="true">
    <defs>
      <radialGradient id="ringFill" gradientUnits="userSpaceOnUse" cx="0" cy="0" r="186">
        <stop offset="0.42" stop-color="#17509c"/>
        <stop offset="0.70" stop-color="#1c5fb6"/>
        <stop offset="0.73" stop-color="#2d82e2"/>
        <stop offset="1" stop-color="#1c5fb6"/>
      </radialGradient>
      <path id="segment" class="segment" d="M0,-186 A186,186 0 0 1 176.9,-57.5 L130.4,-20.6 L74.2,-24.1 A78,78 0 0 0 0,-78 L20.6,-130.4 Z"/>
      <path id="labelTrack" d="M0,-158 A158,158 0 1 1 0,158 A158,158 0 1 1 0,-158"/>
      <g id="lifecycleCog">
        <circle class="cog-teeth" r="191"/>
        <use href="#segment" transform="rotate(-72)"/>
        <use href="#segment"/>
        <use href="#segment" transform="rotate(72)"/>
        <use href="#segment" transform="rotate(144)"/>
        <use href="#segment" transform="rotate(216)"/>
        <circle class="hub" r="78"/>
        <circle class="hub-iris" r="62"/>
        <circle class="hub-orbit" r="44"/>
        <circle class="hub-orbit" r="22"/>
        <circle class="hub-core" r="7"/>
        <text class="ring-label" dominant-baseline="middle" text-anchor="middle"><textPath href="#labelTrack" startOffset="90%">UPGRADE</textPath></text>
        <text class="ring-label" dominant-baseline="middle" text-anchor="middle"><textPath href="#labelTrack" startOffset="10%">EVALUATE</textPath></text>
        <text class="ring-label" dominant-baseline="middle" text-anchor="middle"><textPath href="#labelTrack" startOffset="30%">PROCURE</textPath></text>
        <text class="ring-label" dominant-baseline="middle" text-anchor="middle"><textPath href="#labelTrack" startOffset="50%">IMPLEMENT</textPath></text>
        <text class="ring-label" dominant-baseline="middle" text-anchor="middle"><textPath href="#labelTrack" startOffset="70%">MAINTAIN</textPath></text>
      </g>
    </defs>

    <!-- organic circuit veins linking the two lifecycles -->
    <g class="veins">
      <path class="vein" d="M60,610 C180,560 260,600 380,590 S560,640 640,600 S900,560 1010,590 S1150,640 1200,600"/>
      <path class="vein" d="M0,170 C40,150 70,120 120,118"/>
      <path class="vein" d="M1200,420 C1160,440 1130,470 1100,500"/>
      <path class="vein" d="M30,40 C90,60 120,30 170,30"/>
      <path class="vein" d="M1040,40 C1090,60 1130,30 1180,44"/>
      <circle class="vein-node" cx="380" cy="590" r="4"/>
      <circle class="vein-node" cx="640" cy="600" r="4"/>
      <circle class="vein-node" cx="1010" cy="590" r="4"/>
      <circle class="vein-node" cx="120" cy="118" r="4"/>
      <circle class="vein-node" cx="170" cy="30" r="4"/>
      <circle class="vein-node" cx="1040" cy="40" r="4"/>
    </g>

    <!-- drive chain coupling the two cogs -->
    <line class="drive-chain" x1="257" y1="132" x2="899" y2="132"/>
    <line class="drive-chain" x1="257" y1="514" x2="899" y2="514"/>

    <!-- double-headed connector between the two risk headings -->
    <g class="connector">
      <line x1="372" y1="91" x2="793" y2="91"/>
      <polyline points="381,85 371,91 381,97"/>
      <polyline points="784,85 794,91 784,97"/>
    </g>

    <use href="#lifecycleCog" transform="translate(257 323)"/>
    <use href="#lifecycleCog" transform="translate(899 323)"/>

    <!-- flow arrow carrying the delivery roles -->
    <path class="flow-arrow" d="M475,447 H657 V430 L709,494 L657,560 V540 H475 Z"/>
    <line class="flow-seam" x1="657" y1="447" x2="657" y2="540"/>
    <circle class="flow-rivet" cx="484" cy="456" r="2.5"/>
    <circle class="flow-rivet" cx="484" cy="531" r="2.5"/>
    <circle class="flow-rivet" cx="648" cy="456" r="2.5"/>
    <circle class="flow-rivet" cx="648" cy="531" r="2.5"/>
  </svg>

  <div class="heading heading--procurement">
    <div class="heading-title">Procurement Risk</div>
    <div class="heading-sub">The Right Partner</div>
  </div>
  <div class="heading heading--independence">
    <div class="heading-title">Independence Risk</div>
    <div class="heading-sub">The Right Technology Framework</div>
  </div>
  <div class="heading heading--business">
    <div class="heading-title">Business Risk</div>
    <div class="heading-sub">The Right Outcome</div>
  </div>

  <ul class="domain-list">
    <li>Enterprise Strategy</li>
    <li>Enterprise Software</li>
    <li>Enterprise&nbsp; Hardware</li>
    <li>Enterprise Networks</li>
    <li>Enterprise Services</li>
  </ul>

  <ul class="roles">
    <li>Analysis</li>
    <li>Advisors</li>
    <li>Program Managers</li>
  </ul>

  <div class="brand">
    <span class="brand-square"></span>
    <span class="brand-name">Janet Holm Counsel</span>
  </div>
</main>
</body>
</html>
```